Business Card Design

We need a business card for our established Fruit and Veg shop that offers retail and wholesale to the public. We offer a range of Australian products and also provide nuts, confectionary, pasta's etc. We would like to use colours green, red, orange and yellow. The final design would use our photo of the shop and some produce and should communicate freshness and quality.

Target Market(s)

families, businesses

Industry/Entity Type

Retail

Contact Information for Business Card

Creekbend Produce Shed
Retail and Wholesale Fruit and Veg
Peter and Marco Bellucci - Manager
47 Carrow Valley Road, Penwick Flat S.A. 5172
Ph: (08) 8294 5613
Fax: (08) 8294 5713
creekbendproduceshed@mailbrook.net
www.friendspage.net/CreekbendProduceShed
Open 7 Days

Requirements
Must have
• The photo of the shop
Nice to have
• Both the photos

```html
<!DOCTYPE html>
<html lang="en">
<head>
<meta charset="utf-8">
<title>Creekbend Produce Shed – Business Card</title>
<link rel="stylesheet" href="https://fonts.googleapis.com/css2?family=Open+Sans:wght@400;600;700&display=swap">
<style>
  :root {
    --card-green: #14935f;
    --card-green-deep: #0d7a4c;
    --accent-orange: #f26a2e;
    --accent-lime: #8dc63f;
    --label-text: #2e6b1f;
    --text-white: #ffffff;
    --text-soft: #e8f5ee;
    --page-bg: #ecebe8;
    --photo-produce-a: #b8473f;
    --photo-produce-b: #7d8a4a;
    --photo-shop-a: #4b4f58;
    --photo-shop-b: #9b8f86;
  }
  html, body {
    margin: 0;
    width: 1200px;
    height: 800px;
    overflow: hidden;
    background: var(--page-bg);
    font-family: "Open Sans", Arial, sans-serif;
  }
  .stage {
    position: relative;
    width: 1200px;
    height: 800px;
  }
  .card {
    position: absolute;
    border-radius: 14px;
    overflow: hidden;
    box-shadow: 0 10px 26px rgba(0,0,0,0.22);
    background: var(--card-green);
  }
  .card svg { display: block; }
  .card-front { left: 110px; top: 130px; width: 330px; height: 540px; }
  .card-back  { left: 500px; top: 230px; width: 590px; height: 340px; }
  .brand-name { font-family: "Open Sans", Arial, sans-serif; font-weight: 700; }
  .tagline { font-family: "Open Sans", Arial, sans-serif; font-weight: 400; }
  .contact-text { font-family: "Open Sans", Arial, sans-serif; font-weight: 400; fill: var(--text-white); font-size: 13px; }
  .contact-text.email { font-size: 12px; }
  .person-name { font-family: "Open Sans", Arial, sans-serif; font-weight: 700; fill: var(--accent-orange); font-size: 19px; letter-spacing: 0.4px; }
  .person-role { font-family: "Open Sans", Arial, sans-serif; font-weight: 600; fill: var(--text-white); font-size: 13px; letter-spacing: 1px; }
  .hours-text { font-family: "Open Sans", Arial, sans-serif; font-weight: 600; fill: var(--label-text); font-size: 30px; }
</style>
</head>
<body>
<main class="stage">

  <section class="card card-front" aria-label="Card front">
    <svg width="330" height="540" viewBox="0 0 330 540">
      <defs>
        <linearGradient id="produceFill" x1="0" y1="0" x2="1" y2="1">
          <stop offset="0" stop-color="var(--photo-shop-a)"/>
          <stop offset="0.35" stop-color="var(--photo-produce-a)"/>
          <stop offset="0.7" stop-color="var(--photo-produce-b)"/>
          <stop offset="1" stop-color="var(--photo-produce-a)"/>
        </linearGradient>
        <radialGradient id="frontGlow" cx="0.7" cy="0.3" r="0.8">
          <stop offset="0" stop-color="#1aa56b"/>
          <stop offset="1" stop-color="var(--card-green-deep)"/>
        </radialGradient>
      </defs>
      <rect class="card-bg" width="330" height="540" fill="url(#frontGlow)"/>
      <path class="produce-photo" role="img" aria-label="Photo of fresh apples and produce displays inside the shop"
            d="M0,160 L80,160 C170,230 230,360 210,540 L0,540 Z" fill="url(#produceFill)"/>

      <g class="connector-lines" stroke="var(--accent-orange)" stroke-width="1.6" fill="none">
        <line x1="128" y1="42" x2="222" y2="150"/>
        <line x1="128" y1="272" x2="222" y2="150"/>
        <line x1="222" y1="150" x2="242" y2="150"/>
      </g>

      <g class="hours-label">
        <rect x="70" y="38" width="58" height="236" fill="var(--accent-lime)"/>
        <circle cx="128" cy="42" r="3" fill="var(--label-text)"/>
        <circle cx="128" cy="272" r="3" fill="var(--label-text)"/>
        <text class="hours-text" transform="translate(88,156) rotate(90)" text-anchor="middle">Open 7 Days</text>
      </g>

      <g class="brand-mark" transform="translate(250,150) rotate(90)">
        <text class="brand-name" x="0" y="0" fill="var(--text-white)" font-size="34">Creekbend</text>
        <text class="brand-name" x="20" y="34" fill="var(--text-white)" font-size="26">Produce Shed</text>
        <text class="tagline" x="-6" y="58" fill="var(--text-soft)" font-size="12">Retail and Wholesale Fruit and Veg</text>
      </g>
    </svg>
  </section>

  <section class="card card-back" aria-label="Card back">
    <svg width="590" height="340" viewBox="0 0 590 340">
      <defs>
        <linearGradient id="shopFill" x1="0" y1="0" x2="1" y2="1">
          <stop offset="0" stop-color="var(--photo-shop-a)"/>
          <stop offset="0.5" stop-color="var(--photo-shop-b)"/>
          <stop offset="1" stop-color="#c9c7c2"/>
        </linearGradient>
      </defs>
      <rect class="card-bg" width="590" height="340" fill="var(--card-green)"/>
      <path class="shop-photo" role="img" aria-label="Photo of the shop front with produce on display"
            d="M160,0 L590,0 L590,250 C440,236 260,150 160,0 Z" fill="url(#shopFill)"/>
      <path class="accent-stripe" d="M160,0 C260,150 440,236 590,250 L590,262 C430,250 250,166 148,0 Z"
            fill="var(--accent-orange)"/>

      <g class="brand-mark">
        <text class="brand-name" x="458" y="72" text-anchor="middle" fill="var(--accent-orange)" font-size="34">Creekbend</text>
        <text class="brand-name" x="458" y="104" text-anchor="middle" fill="var(--accent-orange)" font-size="24">Produce Shed</text>
        <text class="tagline" x="458" y="124" text-anchor="middle" fill="var(--text-white)" font-size="12">Retail and Wholesale Fruit and Veg</text>
      </g>

      <g class="contact-list">
        <g class="phone-line">
          <rect x="22" y="22" width="14" height="14" rx="2" fill="var(--accent-orange)"/>
          <path d="M26,25 q-1,4 3,8 q2,1 3,0 l-1.5,-2 l-1.5,1 q-2,-1 -2.5,-3 l1,-1 z" fill="var(--text-white)"/>
          <text class="contact-text" x="44" y="34">(08) 8294 5613</text>
        </g>
        <g class="fax-line">
          <rect x="22" y="44" width="14" height="14" rx="2" fill="var(--accent-orange)"/>
          <rect x="25" y="50" width="8" height="5" fill="var(--text-white)"/>
          <rect x="27" y="46.5" width="4" height="3.5" fill="var(--text-white)"/>
          <text class="contact-text" x="44" y="56">(08) 8294 5713</text>
        </g>
        <g class="email-line">
          <rect x="22" y="66" width="14" height="14" rx="2" fill="var(--accent-orange)"/>
          <rect x="25" y="70" width="8" height="6" fill="none" stroke="var(--text-white)" stroke-width="1"/>
          <path d="M25,70 l4,3 l4,-3" fill="none" stroke="var(--text-white)" stroke-width="1"/>
          <text class="contact-text email" x="44" y="78">creekbendproduceshed@mailbrook.net</text>
        </g>
      </g>

      <g class="person">
        <text class="person-name" x="44" y="222">PETER &amp; MARCO BELLUCCI</text>
        <text class="person-role" x="128" y="242">MANAGER</text>
      </g>

      <g class="address">
        <text class="contact-text" x="338" y="280">47 Carrow Valley Road</text>
        <text class="contact-text" x="338" y="299">Penwick Flat S.A. 5172</text>
        <rect x="338" y="307" width="13" height="13" rx="2" fill="var(--accent-orange)"/>
        <text class="contact-text" x="358" y="318">/CreekbendProduceShed</text>
      </g>
    </svg>
  </section>

</main>
</body>
</html>
```